Harbourline Estates Australia requires a Wordpress themed Real Estate website

Primary design inspiration - http://www.quillstonevue.com.au/

Wordpress install is already set up and ready to go.

See attached for logo and information

Target Market(s)

Property investors

Industry/Entity Type

Real Estate

Font styles to use
Sans Serif

Requirements
Must have
• -A drop down menu at the top to display list of properties which is added via Posts and sorted by post categories (Residential Sales, Residential Lease, Commercial Sales, Commercial Lease and Off-the plan projects)
• -An About us page which states the company profile (see attached)
• An contact us page which has all the contact details (see attached)
Nice to have
• Primary design inspiration - http://www.quillstonevue.com.au/

```html
<!DOCTYPE html>
<html lang="en">
<head>
<meta charset="utf-8">
<title>Harbourline Estates Australia</title>
<link href="https://fonts.googleapis.com/css2?family=Montserrat:wght@400;500;600;700&display=swap" rel="stylesheet">
<style>
:root{
  --green:#2fbf53;
  --green-dark:#27a847;
  --navy:#2c3453;
  --blue-panel:#3c6d99;
  --charcoal:#26292e;
  --charcoal-deep:#1e2125;
  --footer:#222428;
  --paper:#f1f0ee;
  --ink:#2a2d33;
  --muted:#5d6068;
  --white:#ffffff;
  --amber:#f4b400;
  --orange:#f26a2e;
  --sky:#3aa6e0;
  --slate:#3a3f47;
}
*{box-sizing:border-box;margin:0;padding:0}
html,body{width:1200px;height:3261px;overflow:hidden}
body{font-family:"Montserrat",Arial,sans-serif;color:var(--ink);background:var(--white);position:relative}
.abs{position:absolute}
.fill{position:absolute}
/* header / hero */
.hero{left:0;top:0;width:1200px;height:646px;background:linear-gradient(180deg,#2c3257 0%,#3b4a78 45%,#26304d 75%,#141a2c 100%)}
.logo{left:87px;top:30px;display:flex;align-items:center;gap:12px}
.logo-mark{width:30px;height:30px;background:#0b0b0b;border:2px solid var(--white)}
.logo-name{color:var(--white);font-size:14px;font-weight:600;letter-spacing:.5px}
.nav{top:48px;left:304px;display:flex;gap:0;font-size:16px;font-weight:500;color:var(--white)}
.nav a{position:absolute;white-space:nowrap;color:var(--white);text-decoration:none}
.nav .active{color:var(--green)}
.lang{left:1024px;top:38px;width:87px;height:40px;border:2px solid var(--white);border-radius:20px;color:var(--white);font-size:13px;font-weight:600;display:flex;align-items:center;justify-content:center;gap:10px}
.lang span.dot{width:9px;height:9px;border:2px solid var(--white);border-radius:50%}
.hero-title{left:87px;top:305px;color:var(--white);font-size:33px;font-weight:400;letter-spacing:.5px}
.hero-title b{font-weight:700}
.hero-sub{left:87px;top:348px;color:var(--white);font-size:15px}
.btn{background:var(--green);color:var(--white);font-weight:600;border-radius:20px;display:flex;align-items:center;justify-content:center;gap:8px}
.hero-btn{left:87px;top:391px;width:159px;height:34px;font-size:13px}
/* featured */
.featured-text{left:646px;top:718px;width:480px}
.eyebrow{font-size:12px;font-weight:700;letter-spacing:1.5px;text-transform:uppercase}
.eyebrow.blue{color:#3a78a8}
.eyebrow.green{color:var(--green)}
.eyebrow.light{color:var(--white)}
.feat-title{margin-top:20px;font-size:23px;font-weight:600;line-height:31px;color:var(--ink)}
.tag{display:inline-block;font-size:11px;font-weight:700;color:var(--white);padding:3px 14px 3px 10px;clip-path:polygon(0 0,100% 0,88% 100%,0 100%)}
.tag.sale{background:var(--amber)}
.tag.rent{background:var(--slate)}
.tag.buy{background:var(--sky)}
.tag.sold{background:var(--orange)}
.feat-desc{margin-top:16px;font-size:15px;line-height:21px;color:var(--muted);width:440px}
.specs{margin-top:26px;display:flex;gap:30px;font-size:12px;font-weight:600;color:var(--ink)}
.spec{display:flex;align-items:center;gap:8px}
.spec i{width:30px;height:30px;border-radius:50%;background:#3a78a8;display:flex;align-items:center;justify-content:center}
.feat-btn{left:646px;top:1009px;width:111px;height:34px;font-size:13px}
/* tiles */
.tile{top:1109px;width:300px;height:369px}
.tile .tag{position:absolute;left:0;top:58px}
.tile-addr{position:absolute;left:20px;right:20px;top:256px;text-align:center;color:var(--white);font-size:16px;font-weight:500;line-height:22px}
.tile-addr.link{text-decoration:underline}
/* news */
.news-text{left:87px;top:1550px;width:440px;color:var(--white)}
.news-title{margin-top:20px;font-size:21px;font-weight:600;line-height:28px}
.news-body{margin-top:16px;font-size:14px;line-height:22px;opacity:.9}
.arrows{left:87px;top:1830px;display:flex;gap:17px}
.arrow-btn{width:36px;height:36px;border-radius:50%;display:flex;align-items:center;justify-content:center}
.arrow-btn.outline{border:2px solid var(--green)}
.arrow-btn.solid{background:var(--green)}
/* story */
.story-text{left:337px;top:2010px;width:240px;color:var(--white)}
.story-title{margin-top:20px;font-size:21px;font-weight:600;line-height:28px}
.story-body{margin-top:18px;font-size:14px;line-height:22px;opacity:.9}
.story-btn{left:337px;top:2302px;width:111px;height:34px;font-size:13px}
/* contact */
.contact-text{left:87px;top:2658px;color:var(--ink)}
.contact-addr{margin-top:22px;font-size:15px;line-height:21px}
.contact-call{margin-top:20px;font-size:23px;font-weight:500}
.contact-mail{margin-top:6px;font-size:15px}
/* footer */
.f-head{font-size:13px;font-weight:600;letter-spacing:1.5px;color:var(--white);text-transform:uppercase}
.newsletter{left:87px;top:2945px;width:420px}
.newsletter p{margin-top:18px;font-size:13px;line-height:17px;color:#c9cbd0}
.input{margin-top:24px;width:411px;height:36px;border-radius:18px;background:#4b4e55;color:#9a9da4;font-size:13px;font-style:italic;padding-left:24px;display:flex;align-items:center}
.send-btn{margin-top:18px;width:107px;height:34px;font-size:13px}
.quick{left:646px;top:2945px}
.quick ul{list-style:none;margin-top:14px}
.quick li{font-size:13px;line-height:22.5px;color:#c9cbd0}
.quick li.active{color:var(--green)}
.social{left:984px;top:2949px;display:grid;grid-template-columns:repeat(3,32px);gap:16px}
.social span{width:32px;height:32px;border-radius:50%;border:2px solid var(--green)}
.social span.on{background:var(--green)}
.f-rule{left:87px;top:3170px;width:1026px;height:1px;background:#3c3f46}
.copyright{left:87px;top:3206px;font-size:13px;color:#c9cbd0;letter-spacing:.3px}
.to-top{left:1090px;top:3203px}
</style>
</head>
<body>

<!-- Header & hero -->
<section class="fill hero" role="img" aria-label="Night photograph of a harbour with an arch bridge and waterfront city lights"></section>
<div class="abs logo"><span class="logo-mark"></span><span class="logo-name">Harbourline Estates</span></div>
<nav class="abs nav" style="left:0;top:48px">
  <a class="active" style="left:304px">Discover</a>
  <a style="left:413px">Residential &#8964;</a>
  <a style="left:559px">Commercial &#8964;</a>
  <a style="left:715px">Off Plan Projects</a>
  <a style="left:889px">Contact Us</a>
</nav>
<div class="abs lang">ENG <span class="dot"></span></div>
<h1 class="abs hero-title"><b>Harbourline</b> Estates Australia</h1>
<p class="abs hero-sub">We are the team to make your dream come true</p>
<div class="abs btn hero-btn">Discover More</div>

<!-- Featured property -->
<div class="fill" style="left:0;top:646px;width:600px;height:463px;background:linear-gradient(180deg,#9aa3a8 0%,#6f777c 55%,#8a8d8c 100%)" role="img" aria-label="Photograph of a modern two-storey house with timber cladding and a car in the driveway"></div>
<svg class="abs" style="left:262px;top:840px" width="76" height="76" viewBox="0 0 76 76"><circle cx="38" cy="38" r="35" fill="rgba(0,0,0,.25)" stroke="#fff" stroke-width="3"/><path d="M31 25 L53 38 L31 51 Z" fill="#fff"/></svg>
<div class="fill" style="left:600px;top:646px;width:600px;height:463px;background:var(--paper)"></div>
<div class="abs featured-text">
  <div class="eyebrow blue">Featured Properties</div>
  <h2 class="feat-title">4/18 Tidewater Road, Bayview<br>Point, 2027</h2>
  <div style="margin-top:10px"><span class="tag sale">SALE</span></div>
  <p class="feat-desc">Displaying the sense of size, privacy and exclusivity of a house, this stylishly appointed courtyard residence offers a generously ...</p>
  <div class="specs">
    <div class="spec"><i><svg width="16" height="12" viewBox="0 0 16 12"><path d="M1 2v9M1 8h14v3M4 5h11v3" stroke="#fff" stroke-width="2" fill="none"/></svg></i>03 BED</div>
    <div class="spec"><i><svg width="16" height="14" viewBox="0 0 16 14"><path d="M1 6h14v3a4 4 0 0 1-4 4H5a4 4 0 0 1-4-4z" fill="#fff"/><path d="M3 6V2h3" stroke="#fff" stroke-width="2" fill="none"/></svg></i>04 BATH</div>
    <div class="spec"><i><svg width="16" height="12" viewBox="0 0 16 12"><path d="M2 6l2-5h8l2 5v5H2z" fill="#fff"/></svg></i>2 GARAGE</div>
  </div>
</div>
<div class="abs btn feat-btn">More</div>

<!-- Property tiles -->
<div class="abs tile" style="left:0;background:linear-gradient(180deg,#4d6c8e 0%,#8a6a4a 55%,#3e5a52 100%)" role="img" aria-label="Photograph of a stone house with a pool at dusk">
  <span class="tag rent">RENT</span>
  <div class="tile-addr">12 Corella Road, Linden Hill, 2075</div>
</div>
<div class="abs tile" style="left:300px;background:linear-gradient(160deg,#2f9fd0 0%,#1f7aa4 50%,#4bb9b0 100%)" role="img" aria-label="Photograph looking up at a glass office tower">
  <span class="tag sale">SALE</span>
  <div class="tile-addr">1A Larchmont Street, Reed Point, 2027</div>
</div>
<div class="abs tile" style="left:600px;background:linear-gradient(180deg,#2c3036 0%,#3a3a36 55%,#2a3a34 100%)" role="img" aria-label="Darkened photograph of a house at dusk">
  <span class="tag buy">BUY</span>
  <svg style="position:absolute;left:138px;top:170px" width="24" height="20" viewBox="0 0 24 20"><path d="M3 18c0-7 5-11 12-11V2l7 7-7 7v-5C9 11 6 13 3 18z" fill="#fff"/></svg>
  <div class="tile-addr link">19 Ashby Avenue, Marlow Bay, 2030</div>
</div>
<div class="abs tile" style="left:900px;background:linear-gradient(160deg,#9fb4c8 0%,#5c6f85 50%,#2f3d4f 100%)" role="img" aria-label="Photograph of city skyscrapers against a cloudy sky">
  <span class="tag sold">SOLD</span>
  <div class="tile-addr">273 Kestrel Vale Road, Linden Hill, 2075</div>
</div>

<!-- News -->
<div class="fill" style="left:0;top:1478px;width:1200px;height:461px;background:var(--blue-panel)"></div>
<div class="fill" style="left:600px;top:1478px;width:300px;height:461px;background:linear-gradient(180deg,#b8c6d4 0%,#8c9cab 55%,#5e6a74 100%)" role="img" aria-label="Photograph of a businessman on a ladder looking through binoculars over a city"></div>
<div class="abs news-text">
  <div class="eyebrow light">News</div>
  <h3 class="news-title">Lorem Ipsum is simply dummy text of the printing and typesetting.</h3>
  <p class="news-body">Lorem Ipsum has been the industry's standard dummy ever since the 1500s, when an unknown printer took a galley of type and scrambled it to make a type specimen book ...</p>
</div>
<div class="abs arrows">
  <span class="arrow-btn outline"><svg width="14" height="12" viewBox="0 0 14 12"><path d="M13 6H2M6 1L1 6l5 5" stroke="#2fbf53" stroke-width="2" fill="none"/></svg></span>
  <span class="arrow-btn solid"><svg width="14" height="12" viewBox="0 0 14 12"><path d="M1 6h11M8 1l5 5-5 5" stroke="#fff" stroke-width="2" fill="none"/></svg></span>
</div>

<!-- Our story -->
<div class="fill" style="left:0;top:1939px;width:300px;height:648px;background:var(--charcoal)"></div>
<div class="fill" style="left:300px;top:1939px;width:300px;height:463px;background:var(--charcoal-deep)"></div>
<div class="fill" style="left:600px;top:1939px;width:600px;height:648px;background:linear-gradient(160deg,#c9c6bf 0%,#8b8f96 45%,#2f3a4c 80%,#d8d8d6 100%)" role="img" aria-label="Photograph of two businessmen in suits talking at a meeting table"></div>
<div class="fill" style="left:300px;top:2402px;width:300px;height:185px;background:linear-gradient(180deg,#b9bcc0 0%,#e2e2e0 100%)" role="img" aria-label="Photograph of a meeting table with documents and charts"></div>
<div class="abs story-text">
  <div class="eyebrow green">Our Story</div>
  <h3 class="story-title">Harbourline Estates Australia</h3>
  <p class="story-body">Our two offices are located in the heart of Sydney and the heart of Shanghai of China. Our business focus on selling off the plan apartments, terraces, townhouses, , residential units, ....</p>
</div>
<div class="abs btn story-btn">More</div>

<!-- Contact -->
<div class="fill" style="left:0;top:2587px;width:600px;height:287px;background:var(--green)"></div>
<div class="fill" style="left:600px;top:2587px;width:600px;height:287px;background:linear-gradient(135deg,#f1f1f1 0%,#e2e4e6 100%)" role="img" aria-label="Street map showing the office location"></div>
<svg class="abs" style="left:877px;top:2708px" width="26" height="36" viewBox="0 0 26 36"><path d="M13 1C6 1 1 6 1 13c0 9 12 22 12 22s12-13 12-22C25 6 20 1 13 1z" fill="#1b1b1b"/><circle cx="13" cy="13" r="5" fill="#fff"/></svg>
<div class="abs contact-text">
  <div class="eyebrow" style="color:var(--ink)">Contact Us</div>
  <p class="contact-addr">107/25-29 Harlow St Millbrook NSW 2000<br>Australia</p>
  <p class="contact-call">Call: +61 2 9000 4417</p>
  <p class="contact-mail">info@harbourlineestates.com.au</p>
</div>

<!-- Footer -->
<footer class="fill" style="left:0;top:2874px;width:1200px;height:387px;background:var(--footer)"></footer>
<div class="abs newsletter">
  <div class="f-head">Newsletter Sign Up</div>
  <p>Subscribe to our newsletter to get the latest scoop right<br>to your inbox.</p>
  <div class="input">Enter your email ...</div>
  <div class="btn send-btn"><svg width="14" height="14" viewBox="0 0 14 14"><path d="M1 6l12-5-5 12-2-5z" fill="#fff"/></svg>Send</div>
</div>
<div class="abs quick">
  <div class="f-head">Quick Link</div>
  <ul>
    <li>Discover</li>
    <li class="active">Residential</li>
    <li>Commercial</li>
    <li>Off Plan Projects</li>
    <li>Blog</li>
    <li>Contact Us</li>
    <li>Sitemap</li>
  </ul>
</div>
<div class="abs social" aria-label="Social links">
  <span></span><span class="on"></span><span></span>
  <span></span><span></span><span></span>
</div>
<div class="abs f-rule"></div>
<p class="abs copyright">© 2017 Harbourline Estates Australia.  All Rights Reserved</p>
<svg class="abs to-top" width="22" height="22" viewBox="0 0 22 22"><path d="M11 20V4M3 11l8-8 8 8" stroke="#9a9da4" stroke-width="3" fill="none"/></svg>

</body>
</html>
```